Folder outside surface for Marlowe Eye Studios

Hello :
Attached, please see the images and logo that are meant for a 9x12 inch folder. I need a 300dpi file (png, jpeg, and vector) that fits the diagram from a printing company.

```html
<!DOCTYPE html>
<html lang="en">
<head>
<meta charset="utf-8">
<title>Marlowe Eye Studios – Folder Outside Surface</title>
<link href="https://fonts.googleapis.com/css2?family=Lato:wght@400;700;900&display=swap" rel="stylesheet">
<style>
  :root {
    --backdrop: #e2e2e2;
    --paper: #ffffff;
    --navy: #1a3070;
    --navy-panel: #1f3d78;
    --teal: #0e8488;
    --orange: #e85412;
    --text-light: #ffffff;
  }
  * { margin: 0; padding: 0; box-sizing: border-box; }
  html, body {
    width: 1200px;
    height: 1200px;
    overflow: hidden;
    background: var(--backdrop);
    font-family: "Lato", sans-serif;
  }
  .canvas { position: relative; width: 1200px; height: 1200px; }

  .folder-side {
    position: absolute;
    top: 256px;
    width: 515px;
    height: 687px;
    background: var(--paper);
    overflow: hidden;
  }
  .folder-side--back { left: 55px; }
  .folder-side--front { left: 640px; }

  /* Back side: pocket band */
  .pocket-band {
    position: absolute;
    left: 24px;
    top: 479px;
    width: 468px;
    height: 194px;
    background: var(--navy-panel);
    overflow: hidden;
  }
  .pocket-band__waves { position: absolute; inset: 0; width: 100%; height: 100%; }
  .pocket-band__tagline {
    position: absolute;
    top: 56px;
    left: 0;
    width: 100%;
    text-align: center;
    color: var(--text-light);
    font-size: 20px;
    font-weight: 400;
  }
  .pocket-band__brand {
    position: absolute;
    right: 30px;
    top: 126px;
    display: flex;
    align-items: center;
    gap: 8px;
  }
  .brand-dot {
    width: 14px;
    height: 14px;
    border-radius: 50%;
    background: var(--orange);
  }
  .pocket-band__name {
    color: var(--text-light);
    font-size: 15px;
    font-weight: 900;
    letter-spacing: 0.5px;
    text-transform: uppercase;
  }

  /* Front side */
  .cover-waves { position: absolute; inset: 0; width: 100%; height: 100%; }
  .cover-brand {
    position: absolute;
    top: 150px;
    left: 0;
    width: 100%;
    display: flex;
    flex-direction: column;
    align-items: center;
    gap: 18px;
  }
  .cover-brand__mark {
    width: 40px;
    height: 40px;
    border-radius: 50%;
    background: var(--orange);
  }
  .cover-brand__name {
    color: var(--navy);
    font-size: 46px;
    font-weight: 900;
    line-height: 1.05;
    text-align: center;
    text-transform: uppercase;
    letter-spacing: 1px;
  }
  .cover-tagline {
    position: absolute;
    top: 604px;
    left: 0;
    width: 100%;
    text-align: center;
    color: var(--text-light);
    font-size: 18px;
    font-weight: 400;
  }
</style>
</head>
<body>
<main class="canvas">

  <section class="folder-side folder-side--back" aria-label="Folder back">
    <div class="pocket-band">
      <svg class="pocket-band__waves" viewBox="0 0 753 311" preserveAspectRatio="none" aria-hidden="true">
        <path d="M0,109 C60,200 170,280 281,311 L0,311 Z" fill="var(--teal)"/>
        <path d="M0,181 C80,250 180,295 281,311 L0,311 Z" fill="var(--orange)"/>
      </svg>
      <p class="pocket-band__tagline">Trusted Care. Guided by Science.</p>
      <div class="pocket-band__brand">
        <span class="brand-dot"></span>
        <span class="pocket-band__name">Marlowe Eye Studios</span>
      </div>
    </div>
  </section>

  <section class="folder-side folder-side--front" aria-label="Folder front">
    <svg class="cover-waves" viewBox="0 0 829 1106" preserveAspectRatio="none" aria-hidden="true">
      <path d="M0,596 C180,800 470,890 829,888 C600,925 250,880 0,723 Z" fill="var(--teal)"/>
      <path d="M0,745 C180,870 420,930 620,915 C720,908 790,895 829,888 L829,1106 L0,1106 Z" fill="var(--navy)"/>
      <path d="M208,706 C330,790 480,820 580,818 C680,816 760,790 829,745 L829,873 C700,890 560,880 500,863 C380,830 280,770 208,706 Z" fill="var(--orange)"/>
    </svg>
    <div class="cover-brand">
      <span class="cover-brand__mark"></span>
      <h1 class="cover-brand__name">Marlowe<br>Eye Studios</h1>
    </div>
    <p class="cover-tagline">Trusted Care. Guided by Science.</p>
  </section>

</main>
</body>
</html>
```